Exclusive Pet groomer Post Card

We need a design for a direct mailing postcard. We want to include images of some of dogs and cats done the list of our services and the benefits of our company.

I like something like: Does your pet look like any of these or is a similar breed?

If your answer is yes, then it deserves the best groomer in town

any ideas are welcome!
Updates

URGENT Mailing Postcard needed!

Elegant, modern and clean sophisticated card that has images of the dogs and cats provided. I will use the original images from the image bank once the project is approved. As a designer you just need to create the layout for this and the organization!

Thanks

Target Market(s)

High Income professionals that will pay for premium services for their pets.

Industry/Entity Type

Pet

Requirements
Must have
• A full color double sided postcard. 5.5 x 8.5 in postcard. (I want to have all pics uploaded. I used some sample images from stock photo but once approved I will purchase the images at the respective site). Must have space to place recipient address and space for NPDS stamp. ( is a postcard to be mailed!)

I would like to have the following text in the post card:

Enhance the beauty of your pets
Pamper your best friend
Give to your dog or cat the stylish treatment it deserves

One of the top groomers in town
Experienced in dogs and cats
Clean individual pet grooming stations (Sanitation and Sterilization)
Services:
Full service grooming* services for dogs and cats include:
Day Spa, High Fashion Haircuts, hair trimming, nail clipping and “Petticures”
Bathing, gentle ear Cleaning, sanitary trim, Brushing, Fluff Drying and Dematting
* Regular grooming ensures happier and healthier pets

Fur Harbor Trim
2671 SW 87th Avenue, Coral Bend, Florida 33029
T. 305-417-6382
www.furharbortrim.example
Nice to have
• Logo as in the website

```html
<!DOCTYPE html>
<html lang="en">
<head>
<meta charset="utf-8">
<title>Fur Harbor Trim – Postcard Front</title>
<link rel="stylesheet" href="https://fonts.googleapis.com/css2?family=Cinzel:wght@400;700&display=swap">
<style>
  :root {
    --lavender-deep: #9d8cb0;
    --lavender-mid: #b6a9c4;
    --magenta: #b4519f;
    --plum: #a34a92;
    --plum-text: #a04891;
    --violet-ink: #46287a;
    --white: #ffffff;
    --circle-edge: #eae3ee;
  }
  * { margin: 0; padding: 0; box-sizing: border-box; }
  html, body { width: 1200px; height: 851px; overflow: hidden; }
  body { font-family: "Cinzel", "Times New Roman", serif; }

  .postcard {
    position: relative;
    width: 1200px;
    height: 851px;
    overflow: hidden;
    background:
      radial-gradient(ellipse 520px 420px at 640px 560px, #f3eff6 0%, rgba(243,239,246,0) 70%),
      linear-gradient(160deg, var(--lavender-mid) 0%, var(--lavender-deep) 55%, #b3a5c2 100%);
  }

  .photo { position: absolute; }
  .photo--cat {
    left: 435px; top: 160px; width: 416px; height: 691px;
    border-radius: 48% 52% 20% 30% / 22% 24% 10% 10%;
    background: radial-gradient(ellipse at 55% 45%, #fbf7f3 0%, #efe3d8 50%, rgba(222,206,200,0.4) 85%, rgba(222,206,200,0) 100%);
  }
  .photo--dog {
    left: 38px; top: 454px; width: 425px; height: 341px;
    border-radius: 50% 50% 30% 30% / 55% 55% 20% 20%;
    background: radial-gradient(ellipse at 50% 60%, #b0814f 0%, #7a5637 45%, #4a3a33 75%, rgba(74,58,51,0) 100%);
  }

  .bubble {
    position: absolute;
    border-radius: 50%;
    background: radial-gradient(circle at 50% 45%, #ffffff 0%, #ffffff 62%, var(--circle-edge) 100%);
    border: 6px solid rgba(255,255,255,0.9);
    box-shadow: 0 0 0 2px rgba(160,140,180,0.35);
  }
  .bubble--intro { left: -65px; top: -37px; width: 510px; height: 510px; }
  .bubble--benefits { left: 738px; top: 299px; width: 500px; height: 500px; }

  .headline { font-weight: 400; }
  .headline-tab {
    position: absolute; left: 0; top: 0; width: 440px; height: 104px;
    background: var(--magenta);
    color: var(--white);
    font-size: 70px; font-weight: 400; letter-spacing: 2px; text-transform: uppercase;
    display: flex; align-items: center; justify-content: center;
    padding-top: 4px;
  }
  .headline-ribbon { position: absolute; left: 440px; top: 28px; width: 733px; height: 100px; }
  .headline-ribbon svg { position: absolute; inset: 0; }
  .headline-ribbon__text {
    position: relative; display: block;
    color: var(--white); font-size: 42px; font-weight: 400; text-transform: uppercase;
    line-height: 104px; padding-left: 34px; white-space: nowrap;
  }

  .tagline {
    position: absolute; left: 0; top: 128px; width: 380px;
    text-align: center; color: var(--plum-text);
    font-size: 33px; font-weight: 700; line-height: 43px;
  }
  .brand {
    position: absolute; left: 10px; top: 312px; width: 360px;
    text-align: center; white-space: nowrap;
    color: var(--violet-ink); font-size: 30px; font-weight: 700;
  }

  .benefits { color: var(--plum-text); }
  .benefits__title {
    position: absolute; left: 793px; top: 386px; width: 400px;
    text-align: center; font-size: 40px; font-weight: 700; line-height: 42px;
  }
  .benefits__list { position: absolute; left: 862px; top: 515px; width: 330px; list-style: none; }
  .benefits__list li {
    position: relative; padding-left: 32px;
    font-size: 31px; line-height: 30px; margin-bottom: 13px; white-space: nowrap;
  }
  .benefits__list li::before {
    content: ""; position: absolute; left: 0; top: 10px;
    width: 15px; height: 15px; border-radius: 50%; background: var(--magenta);
  }
  .benefits__note { display: block; font-size: 24px; line-height: 27px; }
</style>
</head>
<body>
  <main class="postcard">
    <div class="photo photo--cat" role="img" aria-label="Photo of a white and chocolate point cat walking and looking up"></div>
    <div class="photo photo--dog" role="img" aria-label="Photo of a Yorkshire terrier lying down wearing a pink bow"></div>

    <div class="bubble bubble--intro"></div>
    <div class="bubble bubble--benefits"></div>

    <h1 class="headline">
      <span class="headline-tab">Enhance</span>
      <span class="headline-ribbon">
        <svg width="733" height="100" viewBox="0 0 733 100" aria-hidden="true">
          <polygon points="0,0 733,0 708,50 733,100 0,100" fill="var(--plum)"/>
        </svg>
        <span class="headline-ribbon__text">The beauty of your pets</span>
      </span>
    </h1>

    <p class="tagline">Pamper<br>your best friend</p>
    <p class="brand">Fur Harbor Trim</p>

    <section class="benefits">
      <h2 class="benefits__title">One of the<br>top groomers<br>in town</h2>
      <ul class="benefits__list">
        <li>Experienced in<br>dogs and cats</li>
        <li>Clean individual<br>pet grooming<br>stations
          <span class="benefits__note">(Sanitation and<br>Sterilization)</span></li>
      </ul>
    </section>
  </main>
</body>
</html>
```